letterhead design using our existing logo

We are a small boutique property management business based in Sydney's Northern Beaches.
We are after a sleek, simple modern letterhead (A4) incorporating our logo and its colours.
Also matching envelope (DL)
I have attached the logo with black text and white text for design options.

Target Market(s)

29-69yo Male and Female

Industry/Entity Type

Property Management

Requirements
Must have
• - Keyhaven Estates logo
• - Address, number and website:
• Suite 7, 18-19 Harlow Parade, Brookvale NSW 2100
• Tel: Tom Carrick 0417 293 608 Lorena Adcock 0409 516 742 www.keyhavenestatesgroup.com.au
Nice to have
• sleek design that looks modern and professional
Should not have
• too many colours or too busy

```html
<!DOCTYPE html>
<html lang="en">
<head>
<meta charset="UTF-8">
<title>Keyhaven Estates Letterhead</title>
<link rel="stylesheet" href="https://fonts.googleapis.com/css2?family=Open+Sans:wght@400;600&display=swap">
<style>
  :root {
    --backdrop: #9a9a9a;
    --paper: #ffffff;
    --brand-teal: #0d4353;
    --brand-text: #ffffff;
    --contact-text: #1f4f5e;
  }
  * { box-sizing: border-box; margin: 0; padding: 0; }
  html, body {
    width: 960px;
    height: 1200px;
    overflow: hidden;
  }
  body {
    background: var(--backdrop);
    font-family: "Open Sans", Arial, sans-serif;
    position: relative;
  }
  .letterhead {
    position: absolute;
    left: 70px;
    top: 20px;
    width: 820px;
    height: 1160px;
    background: var(--paper);
  }
  .brand-block {
    position: absolute;
    top: 0;
    right: 38px;
    width: 174px;
    height: 142px;
    background: var(--brand-teal);
    display: flex;
    align-items: flex-end;
    padding: 0 12px 40px 12px;
  }
  .brand-name {
    color: var(--brand-text);
    font-weight: 600;
    font-size: 15px;
    letter-spacing: 0.2px;
    line-height: 1.1;
    text-transform: uppercase;
    white-space: nowrap;
  }
  .contact-details {
    position: absolute;
    top: 152px;
    right: 38px;
    width: 174px;
    padding-left: 2px;
    color: var(--contact-text);
    font-size: 8.6px;
    line-height: 1.45;
    font-style: normal;
  }
  .contact-details p { white-space: nowrap; }
</style>
</head>
<body>
  <main class="letterhead" aria-label="Keyhaven Estates A4 letterhead">
    <header>
      <div class="brand-block">
        <span class="brand-name">Keyhaven Estates</span>
      </div>
      <address class="contact-details">
        <p>Suite 7, 18-19 Harlow Parade</p>
        <p>Brookvale NSW 2100</p>
        <p>Tel: Tom Carrick 0417 293 608</p>
        <p>Lorena Adcock 0409 516 742</p>
        <p>www.keyhavenestatesgroup.com.au</p>
      </address>
    </header>
  </main>
</body>
</html>
```